Creative way to lay out a career advancement graphic

Are you a designer with a knack for turning complex concepts into visually captivating masterpieces? We have an exciting project that needs your unique talent! We're on the lookout for a creative designer to help us visualize our company's diverse career paths. Our organization offers a plethora of opportunities in project management, engineering, sales, and more. We want to showcase these pathways in a visually engaging manner to empower potential job candidates with a clear understanding of their advancement options within our company. Design must be flexible and able to be edited.

Check out the attached examples of the positions we'd like to include in this visualization (doc "inside sales" are correct positions). Your task will be to transform this information into a visually stunning representation that's both informative and inspiring.
This project is not just about design—it's about shaping the narrative of career growth and opportunity within our organization. Your creative input will play a vital role in helping us attract top talent and communicate our company's commitment to fostering professional development. Brand guidelines are also attached for reference. The document titled "parvel" demonstrates a badly done version of what we are trying to achieve. We want to denote multiple routes of advancement. You don't have to get the paths completely correct, you just need to show how it could be approached in a design. For example, A "submittal Specialist" could become a "project manager" but also could ascend to the role of "Industrial Estimator" if they want to move in that direction.

```html
<!DOCTYPE html>
<html lang="en">
<head>
<meta charset="utf-8">
<title>Career Advancement Paths</title>
<link href="https://fonts.googleapis.com/css2?family=Carlito:wght@400;700&display=swap" rel="stylesheet">
<style>
  :root {
    --page: #ffffff;
    --ink: #1b1b1b;
    --gold-top: #f8d81d;
    --gold-mid: #e0b024;
    --gold-bottom: #b37122;
    --node: #e8a23a;
    --brand-ink: #1f2422;
  }
  html, body {
    margin: 0;
    padding: 0;
    overflow: hidden;
    background: var(--page);
  }
  .canvas {
    position: relative;
    width: 849px;
    height: 1200px;
    overflow: hidden;
    background: var(--page);
    font-family: "Carlito", "Calibri", sans-serif;
    color: var(--ink);
  }
  .connectors {
    position: absolute;
    inset: 0;
    width: 849px;
    height: 1200px;
  }
  .role {
    position: absolute;
    box-sizing: border-box;
    width: 238px;
    border: 1.3px solid var(--ink);
    border-radius: 23px;
    background: linear-gradient(180deg, var(--gold-top) 0%, var(--gold-mid) 55%, var(--gold-bottom) 100%);
    display: flex;
    flex-direction: column;
    justify-content: center;
    align-items: center;
    text-align: center;
    padding: 0 8px;
    font-size: 11px;
    line-height: 14.6px;
  }
  .role h2 {
    margin: 0;
    font-size: 11.6px;
    line-height: 14.6px;
    font-weight: 700;
  }
  .role p { margin: 0; }
  .role--top-weighted { padding-bottom: 16px; }

  .brand {
    position: absolute;
    left: 604px;
    top: 40px;
    display: flex;
    align-items: center;
    gap: 8px;
  }
  .brand__dot {
    width: 26px;
    height: 26px;
    border-radius: 50%;
    background: var(--node);
  }
  .brand__name {
    font-size: 34px;
    font-weight: 700;
    letter-spacing: 1px;
    color: var(--brand-ink);
    line-height: 1;
  }
</style>
</head>
<body>
<main class="canvas">

  <svg class="connectors" viewBox="0 0 849 1200" aria-hidden="true">
    <defs>
      <marker id="arrowhead" viewBox="0 0 10 10" refX="9" refY="5" markerWidth="6" markerHeight="6" orient="auto-start-reverse">
        <path d="M0 1 L10 5 L0 9 Z" fill="#1b1b1b"/>
      </marker>
    </defs>
    <g fill="none" stroke="#1b1b1b" stroke-width="1">
      <!-- ladder to sales leadership -->
      <line x1="418" y1="173" x2="418" y2="160" marker-end="url(#arrowhead)"/>
      <line x1="420" y1="309" x2="420" y2="296" marker-end="url(#arrowhead)"/>
      <line x1="424" y1="461" x2="424" y2="433" marker-end="url(#arrowhead)"/>

      <!-- leads converge on outside sales -->
      <path d="M156 508 C160 482 230 479 330 481 C395 482 408 478 418 471" marker-end="url(#arrowhead)"/>
      <line x1="424" y1="508" x2="424" y2="474" marker-end="url(#arrowhead)"/>
      <path d="M693 508 C689 482 620 479 520 480 C455 481 441 478 431 471" marker-end="url(#arrowhead)"/>

      <!-- within-track promotions -->
      <line x1="154" y1="701" x2="154" y2="689" marker-end="url(#arrowhead)"/>
      <line x1="427" y1="700" x2="427" y2="689" marker-end="url(#arrowhead)"/>
      <line x1="429" y1="819" x2="429" y2="808" marker-end="url(#arrowhead)"/>
      <line x1="699" y1="701" x2="699" y2="689" marker-end="url(#arrowhead)"/>

      <!-- entry roles converge -->
      <path d="M260 1040 C262 1015 320 1012 380 1011 C410 1010 418 1005 424 993" marker-end="url(#arrowhead)"/>
      <path d="M594 1040 C592 1015 530 1011 475 1011 C445 1010 436 1005 430 993" marker-end="url(#arrowhead)"/>

      <!-- branch out to the three tracks -->
      <path d="M427 980 C420 955 375 947 270 945 C205 944 168 925 163 884" marker-end="url(#arrowhead)"/>
      <line x1="427" y1="980" x2="427" y2="914" marker-end="url(#arrowhead)"/>
      <path d="M427 980 C434 955 480 947 585 945 C650 944 686 925 690 884" marker-end="url(#arrowhead)"/>
    </g>
    <circle cx="424.5" cy="467" r="5.8" fill="#e8a23a" stroke="#1b1b1b" stroke-width="1"/>
    <circle cx="427" cy="986" r="6.3" fill="#e8a23a" stroke="#1b1b1b" stroke-width="1"/>
  </svg>

  <div class="brand">
    <span class="brand__dot"></span>
    <span class="brand__name">VORLAND</span>
  </div>

  <section class="role" style="left:306px; top:37px; height:121px;">
    <h2>Vice President, Sales</h2>
    <p>Sales strategy development</p>
    <p>Revenue generation</p>
    <p>Market analysis</p>
    <p>Sales forecasting and budgeting</p>
    <p>Team Leadership</p>
  </section>

  <section class="role" style="left:306px; top:173px; height:121px;">
    <h2>Sales Leadership</h2>
    <p>Sets sets goals and targets</p>
    <p>Sales team supervision, mentoring,<br>training and coaching</p>
    <p>Sales strategy development and<br>implementation</p>
  </section>

  <section class="role role--top-weighted" style="left:306px; top:309px; height:122px;">
    <h2>Outside Sales</h2>
    <p>Prospecting and lead generation</p>
    <p>Building and maintaining relationships</p>
    <p>Closing sales and achieving targets</p>
  </section>

  <section class="role role--top-weighted" style="left:37px; top:508px; height:179px;">
    <h2>Lead Project Manager</h2>
    <p>Team leadership, mentoring and training-<br>Project planning and<br>organization- Monitoring &nbsp;and control<br>Customer service and communication<br>Continuous improvement</p>
  </section>

  <section class="role role--top-weighted" style="left:306px; top:508px; height:179px;">
    <h2>Lead Technical Engineer</h2>
    <p>Team leadership, mentoring and training-<br>Technical sales liaison<br>Influence specifications<br>Read &amp; interpret specificationsIndustrial</p>
  </section>

  <section class="role role--top-weighted" style="left:574px; top:508px; height:179px;">
    <h2>Lead Project Engineer</h2>
    <p>Team leadership, mentoring and training<br>Technical expertise + engineering support<br>Subject matter &nbsp;expert relating to<br>job, equipment and commissioning<br>Quality control and project execution-<br>Continuous improvement</p>
  </section>

  <section class="role" style="left:37px; top:701px; height:180px;">
    <h2>Project Manager</h2>
    <p>Project planning and organization<br>Monitoring and control<br>Customer service and communication</p>
  </section>

  <section class="role" style="left:306px; top:700px; height:106px;">
    <h2>Industrial Estimator (Senior)</h2>
    <p>Quote preparation for more complex jobs<br>Specification and drawing review<br>Customer and vendor relationship<br>Analyze competitive pricing- Support<br>outside sales</p>
  </section>

  <section class="role" style="left:306px; top:819px; height:92px;">
    <h2>Industrial Estimator (Junior)</h2>
    <p>Quote preparation for less complex jobs<br>Specification and drawing Review<br>Vendor relationship- Support outside sales</p>
  </section>

  <section class="role" style="left:574px; top:700px; height:180px;">
    <h2>Project Engineer</h2>
    <p>Technical expertise<br>engineering Support<br>Subject matter expert relating to job,<br>equipment and commissioning Quality<br>control and project execution</p>
  </section>

  <section class="role" style="left:176px; top:1040px; height:123px;">
    <h2>Submittal Specialist</h2>
    <p>Document control and management<br>Submittal preparation and review<br>Communication and coordination<br>communication</p>
  </section>

  <section class="role" style="left:435px; top:1040px; height:123px;">
    <h2>Project Coordinator (Gatekeeper)</h2>
    <p>Data entry for projects - Reviews project<br>complexity and assigns accordingly</p>
  </section>

</main>
</body>
</html>
```